Criação de Kit com 5 Layouts de Post para Redes Sociais (Facebook, Instagram e etc) para Construção & Engenharia
A empresa queria:
" Trabalho com a elaboração de projetos de engenharia em geral, sendo o maior foco e experiência os proj. de Prevenção e combate a incêndio, mas tbm na elaboração de projetos arquitetônico, estrutural, e de interiores. Regularização de obras junto a Prefeitura, Corpo de Bombeiros, Junta Ouromar, Vigilância Sanitária. Acompanhamento de Obras. "

```html
<!DOCTYPE html>
<html lang="pt-BR">
<head>
<meta charset="UTF-8">
<title>Post – Engenharia Civil</title>
<link href="https://fonts.googleapis.com/css2?family=Montserrat:wght@300;400;600;700;800&display=swap" rel="stylesheet">
<style>
  :root {
    --ink-green: #1f3a2f;
    --panel-green: #1c3329;
    --gold-light: #e7d3a5;
    --gold-mid: #c9a96a;
    --gold-dark: #a88648;
    --white: #ffffff;
    --photo-dark: #3d4147;
    --photo-mid: #8c8f93;
    --photo-desk: #d8c3a0;
  }
  * { margin: 0; padding: 0; box-sizing: border-box; }
  html, body { width: 1200px; height: 1200px; overflow: hidden; }
  body { font-family: "Montserrat", sans-serif; background: var(--white); }

  .post {
    position: relative;
    width: 1200px;
    height: 1200px;
    overflow: hidden;
  }

  .team-photo {
    position: absolute;
    inset: 0;
    background:
      radial-gradient(ellipse 520px 620px at 720px 500px, var(--photo-desk) 0%, #c8b594 45%, transparent 75%),
      linear-gradient(135deg, var(--photo-mid) 0%, var(--photo-dark) 55%, #2f3338 100%);
  }

  .headline {
    position: absolute;
    left: 130px;
    top: 96px;
    color: var(--ink-green);
    font-size: 37px;
    line-height: 58px;
    text-transform: uppercase;
    letter-spacing: -0.3px;
  }
  .headline .light { font-weight: 300; display: block; }
  .headline .bold { font-weight: 700; display: block; }

  .quote-panel {
    position: absolute;
    left: 0;
    top: 870px;
    width: 600px;
    height: 295px;
    background: linear-gradient(100deg, var(--gold-light) 0%, var(--gold-mid) 55%, var(--gold-dark) 100%);
    clip-path: polygon(0 0, 92% 0, 100% 100%, 0 100%);
    padding: 38px 0 0 90px;
    color: var(--ink-green);
    z-index: 2;
  }
  .quote-title {
    font-size: 31px;
    font-weight: 800;
    line-height: 36px;
    text-transform: uppercase;
    margin-bottom: 22px;
  }
  .contact-list { list-style: none; }
  .contact-list li {
    display: flex;
    align-items: center;
    gap: 18px;
    font-size: 25px;
    font-weight: 400;
    line-height: 40px;
  }
  .contact-list svg { width: 24px; height: 24px; fill: var(--ink-green); flex: none; }

  .brand-panel {
    position: absolute;
    left: 480px;
    top: 890px;
    width: 720px;
    height: 240px;
    background: var(--pang, var(--panel-green));
    display: flex;
    flex-direction: column;
    align-items: center;
    justify-content: center;
    padding-left: 110px;
    z-index: 1;
  }
  .brand-name {
    display: flex;
    align-items: center;
    gap: 18px;
    color: var(--white);
    font-size: 38px;
    font-weight: 400;
    letter-spacing: 5px;
    text-transform: uppercase;
  }
  .brand-mark {
    width: 22px;
    height: 22px;
    background: var(--gold-mid);
  }
  .brand-tagline {
    margin-top: 12px;
    color: var(--gold-mid);
    font-size: 15px;
    font-weight: 400;
    letter-spacing: 3px;
    text-transform: uppercase;
  }
</style>
</head>
<body>
  <main class="post">
    <div class="team-photo" role="img" aria-label="Vista de cima de uma equipe de engenheiros em volta de uma mesa com plantas técnicas, capacete azul, calculadora e notebook"></div>

    <h1 class="headline">
      <span class="light">O engenheiro civil</span>
      <span class="bold">é o profissional capaz</span>
      <span class="light">de olhar o que todos</span>
      <span class="bold">ignoram e saber como</span>
      <span class="light">resolver qualquer problema.</span>
    </h1>

    <section class="quote-panel">
      <h2 class="quote-title">Peça seu<br>orçamento</h2>
      <ul class="contact-list">
        <li>
          <svg viewBox="0 0 24 24"><circle cx="12" cy="12" r="12"/><path d="M8.2 6.5l1.8-.4 1.2 2.7-1.3 1c.7 1.5 1.8 2.6 3.3 3.3l1-1.3 2.7 1.2-.4 1.8c-.2.6-.7 1-1.4 1C10.9 15.8 8.2 13.1 8.2 8c0-.7.4-1.3 1-1.5z" fill="#d9bf87"/></svg>
          (00) 0000-0000
        </li>
        <li>
          <svg viewBox="0 0 24 24"><circle cx="12" cy="12" r="12"/><path d="M8.2 6.5l1.8-.4 1.2 2.7-1.3 1c.7 1.5 1.8 2.6 3.3 3.3l1-1.3 2.7 1.2-.4 1.8c-.2.6-.7 1-1.4 1C10.9 15.8 8.2 13.1 8.2 8c0-.7.4-1.3 1-1.5z" fill="#d9bf87"/></svg>
          (00) 0000-0000
        </li>
        <li>
          <svg viewBox="0 0 24 24"><circle cx="12" cy="12" r="12"/><rect x="6" y="8" width="12" height="8.5" rx="1" fill="#d9bf87"/><path d="M6.5 8.6l5.5 4.2 5.5-4.2" fill="none" stroke="#1f3a2f" stroke-width="1.4"/></svg>
          email@email.com.br
        </li>
      </ul>
    </section>

    <section class="brand-panel">
      <div class="brand-name"><span class="brand-mark"></span>Helena Varani</div>
      <p class="brand-tagline">Projetando com qualidade e segurança</p>
    </section>
  </main>
</body>
</html>
```